Dune Air & Plus business card

I need an awesome, double-sided business card designed with our new logo. I would like the one side black with the colored logo, and the back side is all yours. I'd like to see horizontal and vertical layouts. Get creative! Thank you.

Target Market(s)

HVAC, Heating and Cooling in Phoenix, AZ

Industry/Entity Type

HVAC

Contact Information for Business Card

We need our new logo on the card. Tom Harker, (623) 555-0142, tom@trydunesair.com, www.trydunesair.com, ROC 514273

```html
<!DOCTYPE html>
<html lang="en">
<head>
<meta charset="utf-8">
<title>Dune Air &amp; Plus — Business Card</title>
<link rel="stylesheet" href="https://fonts.googleapis.com/css2?family=Krona+One&family=Michroma&display=swap">
<style>
  :root {
    --stage: #b2b2b2;
    --card-front: #ffffff;
    --card-back: #222224;
    --ink: #333335;
    --brand-blue: #2a7cc7;
    --brand-orange: #ef7b38;
    --white: #ffffff;
  }
  * { margin: 0; padding: 0; box-sizing: border-box; }
  html, body { width: 1000px; height: 1200px; overflow: hidden; }
  body { background: var(--stage); position: relative; font-family: "Michroma", sans-serif; }

  .card { position: absolute; left: 50px; width: 899px; height: 540px; }
  .card--front { top: 43px; background: var(--card-front); }
  .card--back { top: 617px; height: 539px; background: var(--card-back); }

  .brand { position: absolute; display: flex; align-items: center; }
  .brand__mark { border-radius: 50%; background: var(--brand-orange); flex: none; }
  .brand__name { font-family: "Michroma", sans-serif; font-weight: 400; color: var(--brand-blue); line-height: 1.15; white-space: nowrap; }

  .card--front .brand { left: 84px; top: 150px; width: 330px; height: 240px; justify-content: center; gap: 18px; }
  .card--front .brand__mark { width: 46px; height: 46px; }
  .card--front .brand__name { font-size: 38px; }

  .card--back .brand { left: 0; right: 0; top: 140px; height: 260px; justify-content: center; gap: 24px; }
  .card--back .brand__mark { width: 60px; height: 60px; }
  .card--back .brand__name { font-size: 50px; }

  .holder { position: absolute; left: 502px; top: 170px; font-family: "Krona One", sans-serif; font-weight: 400; font-size: 33px; color: var(--ink); white-space: nowrap; }

  .contacts { position: absolute; left: 502px; top: 223px; list-style: none; }
  .contacts li { display: flex; align-items: center; height: 26px; margin-bottom: 17.5px; font-size: 23px; color: var(--ink); white-space: nowrap; }
  .contacts .icon { width: 26px; height: 26px; background: var(--brand-blue); border-radius: 3px; margin-right: 9px; display: flex; align-items: center; justify-content: center; flex: none; }
  .contacts .icon svg { width: 17px; height: 17px; }
  .contacts .no-icon { padding-left: 35px; }

  .social { position: absolute; left: 685px; top: 454px; display: flex; gap: 12px; }
  .social__item { width: 47px; height: 47px; background: var(--brand-blue); display: flex; align-items: center; justify-content: center; }
  .social__item svg { width: 28px; height: 28px; }
</style>
</head>
<body>
  <section class="card card--front">
    <div class="brand">
      <span class="brand__mark"></span>
      <span class="brand__name">Dune Air<br>&amp; Plus</span>
    </div>

    <h1 class="holder">Tom Harker</h1>

    <ul class="contacts">
      <li><span class="icon"><svg viewBox="0 0 24 24" fill="none" stroke="#fff" stroke-width="2"><path d="M6 3h3l1.5 4-2 1.5a11 11 0 0 0 7 7l1.5-2 4 1.5v3a2 2 0 0 1-2 2A17 17 0 0 1 4 5a2 2 0 0 1 2-2z"/></svg></span>(623) 555-0142</li>
      <li><span class="icon"><svg viewBox="0 0 24 24" fill="none" stroke="#fff" stroke-width="2"><rect x="3" y="6" width="18" height="12"/><path d="M3 6l9 7 9-7M3 18l7-6M21 18l-7-6"/></svg></span>tom@trydunesair.com</li>
      <li><span class="icon"><svg viewBox="0 0 24 24" fill="none" stroke="#fff" stroke-width="1.8"><circle cx="12" cy="12" r="9"/><ellipse cx="12" cy="12" rx="4" ry="9"/><path d="M3 12h18M5 7h14M5 17h14"/></svg></span>www.trydunesair.com</li>
      <li class="no-icon">ROC 514273</li>
    </ul>

    <div class="social" aria-label="Social profiles">
      <span class="social__item"><svg viewBox="0 0 24 24" fill="none" stroke="#fff" stroke-width="2"><path d="M4 5h16v11H9l-5 4z"/></svg></span>
      <span class="social__item"><svg viewBox="0 0 24 24" fill="none" stroke="#fff" stroke-width="2"><circle cx="6" cy="12" r="2.5"/><circle cx="18" cy="6" r="2.5"/><circle cx="18" cy="18" r="2.5"/><path d="M8.2 10.9l7.6-3.8M8.2 13.1l7.6 3.8"/></svg></span>
      <span class="social__item"><svg viewBox="0 0 24 24" fill="none" stroke="#fff" stroke-width="2"><circle cx="12" cy="8" r="4"/><path d="M4 21c0-4.4 3.6-7 8-7s8 2.6 8 7"/></svg></span>
    </div>
  </section>

  <section class="card card--back">
    <div class="brand">
      <span class="brand__mark"></span>
      <span class="brand__name">Dune Air<br>&amp; Plus</span>
    </div>
  </section>
</body>
</html>
```